Business Card Design

Attached is the logo of the store.

Information needed on the business card:

www.vault82vino.com
info@vault82vino.com
412 7th Ave NY, NY 10036
Tel:(646) 555-0147

Store Hours
Mon-Sat Noon-10pm
Sun Noon-8pm

Free Deliveries

Industry/Entity Type

Business

Contact Information for Business Card

Bramble 82 Wine & Spirits

```html
<!DOCTYPE html>
<html lang="en">
<head>
<meta charset="utf-8">
<title>Bramble 82 Wine &amp; Spirits — Business Card</title>
<link href="https://fonts.googleapis.com/css2?family=Open+Sans:wght@400;600&display=swap" rel="stylesheet">
<style>
  :root {
    --backdrop: #3b332f;
    --card: #161616;
    --card-edge: #222;
    --ink: #f2f2f2;
    --silver: #9a9a9a;
    --silver-soft: #5a5a5a;
    --accent: #d4213d;
  }
  * { box-sizing: border-box; margin: 0; padding: 0; }
  html, body { width: 1200px; height: 716px; overflow: hidden; }
  body {
    background: var(--backdrop);
    font-family: "Open Sans", Arial, sans-serif;
    display: flex;
    align-items: center;
    justify-content: center;
    gap: 48px;
  }
  .card {
    width: 525px;
    height: 300px;
    background: var(--card);
    border: 1px solid var(--card-edge);
    position: relative;
    overflow: hidden;
  }
  .card-front {
    display: flex;
    align-items: center;
    justify-content: center;
  }
  .brand-mark {
    display: flex;
    align-items: center;
    gap: 14px;
    color: var(--silver-soft);
    font-weight: 400;
    font-size: 52px;
    letter-spacing: 1px;
  }
  .brand-dot {
    width: 22px; height: 22px;
    border-radius: 50%;
    background: var(--silver-soft);
  }
  .card-back .details {
    position: absolute;
    left: 30px;
    top: 26px;
    color: var(--ink);
  }
  .brand-small {
    font-size: 22px;
    font-weight: 400;
    color: var(--ink);
    letter-spacing: .5px;
    margin-bottom: 8px;
  }
  .person-name { font-size: 15px; margin-bottom: 6px; }
  .contact-list { list-style: none; font-size: 10.5px; line-height: 1.75; }
  .contact-list li { display: flex; align-items: center; gap: 7px; }
  .contact-list svg { width: 9px; height: 9px; fill: var(--accent); }
  .address {
    font-size: 10.5px;
    border-top: 1px solid #555;
    margin-top: 4px;
    padding-top: 4px;
  }
  .hours {
    margin-top: 8px;
    color: var(--accent);
    font-size: 10.5px;
    line-height: 1.45;
  }
  .back-mark {
    position: absolute;
    right: 60px;
    top: 80px;
    width: 170px;
    height: 170px;
    border-radius: 50%;
    border: 10px solid var(--silver);
  }
</style>
</head>
<body>
  <section class="card card-front" aria-label="Card front">
    <div class="brand-mark"><span class="brand-dot"></span><span>Bramble 82</span></div>
  </section>

  <section class="card card-back" aria-label="Card back">
    <div class="details">
      <p class="brand-small">Bramble 82</p>
      <p class="person-name">Your Name</p>
      <ul class="contact-list">
        <li><svg viewBox="0 0 10 10"><rect x="2" y="0" width="6" height="10" rx="1.5"/></svg>(646) 555-0147</li>
        <li><svg viewBox="0 0 10 10"><rect x="0" y="1.5" width="10" height="7" rx="1"/></svg>info@vault82vino.com</li>
        <li><svg viewBox="0 0 10 10"><circle cx="5" cy="5" r="5"/></svg>www.vault82vino.com</li>
      </ul>
      <p class="address">412 7th Ave NY, NY 10036</p>
      <p class="hours">Store Hours<br>Mon-Sat Noon-10pm<br>Sun Noon-8pm<br>Free Deliveries</p>
    </div>
    <div class="back-mark" role="img" aria-label="Large store mark"></div>
  </section>
</body>
</html>
```